Bright Tutor Circle business card

Use existing logo to design a business card which contains information that is listed below. Use of logo as attached. It is important that the colour scheme matches the logo already designed. It needs to be crisp and professional. This is an on line business, a database of training providers for educational establishments. The website will provide users with full information on trainers who are available and their credibility.
Target Market(s)
Educators and training providers
Industry/Entity Type
Education
Contact Information for Business Card
See below for details
Font styles to use
Colors
Designer to choose colors to be used in the design.
Requirements
Must have
- Email address mara@brighttutorcircle.co.uk
- Twitter feed. @MaraBtc
- LinkedIn details Mara Fenwick
- Mobile phone number 07812 540913
- Mission statement: To create a learning network that ensures that schools receive first class training that is excellent value for money.
Nice to have
- N/a
Should not have
- Twee educational images

```html
<!DOCTYPE html>
<html lang="en">
<head>
<meta charset="utf-8">
<title>Bright Tutor Circle – Business Card</title>
<link rel="stylesheet" href="https://fonts.googleapis.com/css2?family=Montserrat:wght@500;600&family=Work+Sans:wght@400;500&display=swap">
<style>
  :root {
    --backdrop: #262626;
    --card: #1c1c1d;
    --card-edge: #2b2b2c;
    --brand-blue: #1e9be0;
    --ink: #f2f2f2;
    --ink-soft: #d9d9d9;
  }
  * { box-sizing: border-box; margin: 0; padding: 0; }
  html, body { width: 1200px; height: 900px; overflow: hidden; }
  body {
    background: var(--backdrop);
    display: flex;
    flex-direction: column;
    align-items: center;
    justify-content: center;
    gap: 40px;
    font-family: "Work Sans", Arial, sans-serif;
  }
  .card {
    position: relative;
    width: 700px;
    height: 390px;
    background: linear-gradient(135deg, var(--card-edge), var(--card) 60%);
    border-bottom: 7px solid var(--brand-blue);
    box-shadow: 0 14px 30px rgba(0,0,0,0.45);
  }
  .brand {
    display: flex;
    align-items: center;
    gap: 14px;
    font-family: "Montserrat", Arial, sans-serif;
    font-weight: 600;
    color: var(--brand-blue);
    text-transform: uppercase;
  }
  .brand-dot {
    border-radius: 50%;
    background: var(--brand-blue);
    flex: none;
  }

  /* Mission side */
  .card--mission {
    display: flex;
    flex-direction: column;
    align-items: center;
    justify-content: center;
    text-align: center;
    padding: 0 50px;
  }
  .card--mission .brand { font-size: 38px; letter-spacing: 0.5px; margin-bottom: 44px; }
  .card--mission .brand-dot { width: 52px; height: 52px; }
  .mission-title {
    font-family: "Montserrat", Arial, sans-serif;
    font-weight: 500;
    color: var(--brand-blue);
    font-size: 19px;
    letter-spacing: 0.5px;
    margin-bottom: 6px;
  }
  .mission-text {
    color: var(--ink);
    font-size: 16px;
    font-weight: 500;
    line-height: 1.35;
  }

  /* Contact side */
  .card--contact {
    display: flex;
    align-items: center;
    padding: 0 50px 0 55px;
  }
  .card--contact .brand { font-size: 25px; width: 270px; }
  .card--contact .brand-dot { width: 38px; height: 38px; }
  .divider {
    width: 2px;
    height: 130px;
    background: var(--brand-blue);
    margin: 0 34px 0 24px;
  }
  .person-name {
    font-family: "Montserrat", Arial, sans-serif;
    font-weight: 600;
    color: var(--brand-blue);
    font-size: 28px;
    letter-spacing: 0.5px;
    text-transform: uppercase;
    line-height: 1;
  }
  .person-role {
    color: var(--ink-soft);
    font-size: 17px;
    margin: 4px 0 16px;
  }
  .contact-list { list-style: none; }
  .contact-item {
    display: flex;
    align-items: center;
    gap: 12px;
    color: var(--ink);
    font-size: 17px;
    line-height: 1.45;
  }
  .contact-icon { width: 14px; height: 14px; flex: none; }
  .contact-dot {
    width: 10px; height: 10px; margin: 0 2px;
    border-radius: 50%; background: var(--brand-blue); flex: none;
  }
</style>
</head>
<body>
  <section class="card card--mission">
    <div class="brand"><span class="brand-dot"></span>Bright Tutor Circle</div>
    <h2 class="mission-title">MISSION STATEMENT:</h2>
    <p class="mission-text">To create a learning network that ensures that schools receive first class<br>training that is excellent value for money.</p>
  </section>

  <section class="card card--contact">
    <div class="brand"><span class="brand-dot"></span>Bright Tutor Circle</div>
    <span class="divider"></span>
    <div class="person">
      <h1 class="person-name">Daniel Hartley</h1>
      <p class="person-role">Director</p>
      <ul class="contact-list">
        <li class="contact-item">
          <svg class="contact-icon" viewBox="0 0 24 24" aria-hidden="true"><path fill="#1e9be0" d="M6.6 10.8c1.4 2.8 3.8 5.1 6.6 6.6l2.2-2.2c.3-.3.7-.4 1-.2 1.1.4 2.3.6 3.6.6.6 0 1 .4 1 1V20c0 .6-.4 1-1 1C10.6 21 3 13.4 3 4c0-.6.4-1 1-1h3.5c.6 0 1 .4 1 1 0 1.3.2 2.5.6 3.6.1.3 0 .7-.2 1z"/></svg>
          07812 540913
        </li>
        <li class="contact-item"><span class="contact-dot"></span>@MaraBtc</li>
        <li class="contact-item"><span class="contact-dot"></span>Mara Fenwick</li>
        <li class="contact-item">
          <svg class="contact-icon" viewBox="0 0 24 24" aria-hidden="true"><rect x="2.5" y="5" width="19" height="14" rx="1.5" fill="none" stroke="#1e9be0" stroke-width="2"/><path d="M3 6l9 7 9-7" fill="none" stroke="#1e9be0" stroke-width="2"/></svg>
          mara@brighttutorcircle.co.uk
        </li>
      </ul>
    </div>
  </section>
</body>
</html>
```